Gaming company needs web presence

PLEASE NOTE: We need just a simple web site. We are at least a year away from launching our first product, so the site only needs a small amount of information on it. The only people who will be visiting the web site are prospective employees, prospective investors who want a little information on the company, journalists who want a little more information, and people in the games industry who will visit to read blog posts about the development of our first game.

Brindlewick Games is a new gaming company that wants to change how people think about video games. We are making games that we think can be so interesting to watch that people might want to tune into them instead of the TV.

The games we make are sophisticated, they are not for children, and we want to project an image of being serious about our craft and the brand we're trying to create. Our games are heavily focused on players interacting with each other in sophisticated ways: to negotiate, to compete, to fight, to come to each other's rescue, to cheer each other on, or to simply watch each other in awe.

We do not want a site that features lots of video game cliches like joysticks, 8 bit graphics, science fiction themes, or military themes. We are focused on craftsmanship, so we'd like to project a sense of precision, pride and deep purpose.

The purpose of this website is to create an image of our company that can help us recruit like-minded craftspeople and help find business partners. There will be no e-commerce, account creation, or forums for some time. The site should have:
-A front page that describes our business
-A section that describes our first game (we have only one for now)
-A section for employees to write blog posts. There should be something on the home page that shows links to the latest 3 blog posts.
-A section about founders that shows information about them.
-Contact information, lets people send us email

Our first game is one that looks very realistic. It takes place on a tropical island. We can't say a lot more about it in public yet, but I will say these things: it is not a game that children will play, it is not very violent, it would look more like a film than a typical video game.

And the site should be easily extendable when we have more content and more categories of content.

I've attached our official company logo with a color scheme we've been using, plus an alternate version of the logo. Please use this as a starting point for the web site's visual design. Also, I do not think it is necessary to use the dark background in the logo as the background throughout the site. I wouldn't rule it out, but I'd like to see some proposals with lighter backgrounds.

We need to be able to get code from you so that we can drop it on our server and get it running without extra effort. We need to be able to add content for Blog posts easily as well, so please indicate how that would work.
Updates

Hello everyone, Thanks for all of the great submissions so far. There are some important things I'd like to relay to everyone: We are at least a year away from launching our first game, so we only need a simple web site. Unfortunately, we can't share any screenshots or details about our first game yet. All of these submissions look great, but are far too complicated. Also, I really want to stress that we don't want to feature stock photography of people playing games, especially of children playing games. In fact, since we don't want to release any screenshots of our games and we don't have any good photography of ourselves working, it's best if there are no photographic images on the site for now.

Hello designers, Can you let me know if your designs include all the code that would let us drop the files on to our web server and easily get it up and running? Also, can you tell me how the blog posts would be created? Does your code run on a CMS? Thanks, Hollis

Hi Designers, we will be hosting this site with Wordpress, so we would prefer to have submissions ready to go on a Wordpress server. Thanks!

Target Market(s)

Investors, prospective employees, press, blog post readers.

Industry/Entity Type

Business

Font styles to use
Sans Serif

Requirements
Must have
• Simplicity first. Please use a color palette and fonts that match our logo.
Should not have
• Video game cliches. Flash animations or menus.
No children.
No photographs of people playing games.

(I realize this is very limiting, but we're keeping the sits as simple as possible for now)

```html
<!DOCTYPE html>
<html lang="en">
<head>
<meta charset="utf-8">
<title>Brindlewick Games – Blog</title>
<link href="https://fonts.googleapis.com/css2?family=Roboto:wght@400;700;900&display=swap" rel="stylesheet">
<style>
  :root {
    --page-bg: #e9e9e9;
    --nav-bg: #3a2418;
    --nav-text: #f1e6dc;
    --accent: #e2731f;
    --ink: #2b211c;
    --muted: #8a8581;
    --rule: #dedad6;
    --paper: #ffffff;
    --earth-dark: #4a2a17;
    --earth-mid: #8c4e22;
    --earth-light: #c9813d;
  }
  * { box-sizing: border-box; margin: 0; padding: 0; }
  html, body { width: 800px; height: 1200px; overflow: hidden; }
  body {
    background: var(--page-bg);
    font-family: "Roboto", Arial, sans-serif;
    color: var(--ink);
    position: relative;
  }
  .mockup {
    position: absolute;
    left: 59px;
    width: 682px;
    background: var(--paper);
    box-shadow: 0 1px 4px rgba(0,0,0,.18);
    overflow: hidden;
  }
  .mockup--index { top: 27px; height: 426px; }
  .mockup--all { top: 507px; height: 626px; }

  .site-nav {
    height: 22px;
    background: var(--nav-bg);
    display: flex;
    align-items: center;
    padding: 0 26px 0 170px;
    font-size: 8px;
    font-weight: 700;
    letter-spacing: .5px;
  }
  .site-nav a {
    color: var(--nav-text);
    text-decoration: none;
    padding: 0 12px;
    height: 22px;
    line-height: 22px;
  }
  .site-nav a.is-current { background: var(--accent); color: #fff; }
  .site-nav .social { margin-left: auto; display: flex; gap: 8px; align-items: center; }
  .social-item { display: flex; align-items: center; gap: 4px; color: var(--nav-text); font-size: 7px; }
  .social-item span.box { width: 10px; height: 10px; background: var(--nav-text); display: block; }

  .earth-top {
    height: 28px;
    background: linear-gradient(180deg, var(--earth-dark) 0%, var(--earth-mid) 55%, rgba(201,129,61,.25) 85%, rgba(255,255,255,0) 100%);
  }
  .earth-bottom {
    position: absolute; left: 0; right: 0; bottom: 0;
    height: 48px;
    background: linear-gradient(180deg, rgba(255,255,255,0) 0%, var(--earth-light) 25%, var(--earth-mid) 60%, var(--earth-dark) 100%);
  }

  .section-title {
    display: flex; align-items: center; justify-content: center;
    gap: 14px;
    margin: 14px 0 16px;
  }
  .section-title::before, .section-title::after {
    content: ""; width: 130px; height: 1px; background: var(--accent);
  }
  .section-title h1 {
    font-size: 15px; font-weight: 900; letter-spacing: 1px;
    color: var(--accent);
    border-top: 2px solid var(--accent);
    border-bottom: 2px solid var(--accent);
    padding: 2px 14px;
  }

  .post-grid {
    display: grid;
    grid-template-columns: repeat(3, 1fr);
    column-gap: 36px;
    row-gap: 22px;
    padding: 0 54px;
  }
  .post-card { border-bottom: 1px solid var(--rule); padding-bottom: 8px; }
  .post-date {
    font-size: 8px; color: var(--accent); font-weight: 700;
    border-bottom: 1px solid var(--rule); padding-bottom: 4px; margin-bottom: 6px;
  }
  .post-title { font-size: 11.5px; font-weight: 700; line-height: 1.25; height: 30px; margin-bottom: 8px; }
  .post-excerpt { font-size: 7.5px; line-height: 1.55; color: var(--muted); height: 82px; overflow: hidden; }
  .read-more {
    display: block; text-align: right; font-size: 6.5px; font-weight: 700;
    color: var(--ink); text-decoration: none; letter-spacing: .4px; margin-top: 8px;
  }
  .earlier-posts {
    display: block; width: 72px; margin: 26px auto 0;
    border: 1px solid var(--rule); text-align: center;
    font-size: 6.5px; color: var(--muted); padding: 4px 0; letter-spacing: .4px;
  }
  .caption {
    position: absolute; right: 59px;
    font-size: 9px; color: #6a6663;
  }
  .caption--index { top: 458px; }
  .caption--all { top: 1139px; }
</style>
</head>
<body>

<section class="mockup mockup--index" aria-label="Brindlewick Games blog on the index page">
  <nav class="site-nav">
    <a class="is-current" href="#">BLOG</a><a href="#">ABOUT US</a><a href="#">GAMES</a><a href="#">CONTACT</a>
    <div class="social">
      <div class="social-item"><span class="box"></span>2.5K</div>
      <div class="social-item"><span class="box"></span>1.2K</div>
    </div>
  </nav>
  <div class="earth-top" role="img" aria-label="Rough earth-toned texture band"></div>
  <div class="section-title"><h1>BLOG</h1></div>
  <div class="post-grid">
    <article class="post-card">
      <p class="post-date">21.05.2014</p>
      <h2 class="post-title">DevSummit14 Procedural Animation Video available!</h2>
      <p class="post-excerpt">Our talk on procedural animation is now online for everyone. We walk through the rig, the solver and the many small choices that made our characters move with weight and intent.</p>
      <a class="read-more" href="#">READ MORE</a>
    </article>
    <article class="post-card">
      <p class="post-date">18.05.2014</p>
      <h2 class="post-title">We're on IndieHub!</h2>
      <p class="post-excerpt">Our studio page is now live, where you can follow progress on our first game. Expect regular notes from the team on art, systems and the craft behind each feature we build.</p>
      <a class="read-more" href="#">READ MORE</a>
    </article>
    <article class="post-card">
      <p class="post-date">12.05.2014</p>
      <h2 class="post-title">DevSummit14 Summary Animation Bootcamp Part 4/6</h2>
      <p class="post-excerpt">The fourth part of our summary covers blending, foot planting and timing. We share what we learned from the sessions and how it shapes the way our own animators work each day.</p>
      <a class="read-more" href="#">READ MORE</a>
    </article>
  </div>
  <a class="earlier-posts" href="#">EARLIER POSTS</a>
  <div class="earth-bottom" role="img" aria-label="Rough earth-toned texture band"></div>
</section>
<p class="caption caption--index">Blog view (scrolled down the index page)</p>

<section class="mockup mockup--all" aria-label="Brindlewick Games blog with all posts">
  <nav class="site-nav">
    <a class="is-current" href="#">BLOG</a><a href="#">ABOUT US</a><a href="#">GAMES</a><a href="#">CONTACT</a>
    <div class="social">
      <div class="social-item"><span class="box"></span>2.5K</div>
      <div class="social-item"><span class="box"></span>1.2K</div>
    </div>
  </nav>
  <div class="earth-top" role="img" aria-label="Rough earth-toned texture band"></div>
  <div class="section-title"><h1>BLOG</h1></div>
  <div class="post-grid">
    <article class="post-card">
      <p class="post-date">21.05.2014</p>
      <h2 class="post-title">DevSummit14 Procedural Animation Video available!</h2>
      <p class="post-excerpt">Our talk on procedural animation is now online for everyone. We walk through the rig, the solver and the many small choices that made our characters move with weight and intent.</p>
      <a class="read-more" href="#">READ MORE</a>
    </article>
    <article class="post-card">
      <p class="post-date">18.05.2014</p>
      <h2 class="post-title">We're on IndieHub!</h2>
      <p class="post-excerpt">Our studio page is now live, where you can follow progress on our first game. Expect regular notes from the team on art, systems and the craft behind each feature we build.</p>
      <a class="read-more" href="#">READ MORE</a>
    </article>
    <article class="post-card">
      <p class="post-date">12.05.2014</p>
      <h2 class="post-title">DevSummit14 Summary Animation Bootcamp Part 4/6</h2>
      <p class="post-excerpt">The fourth part of our summary covers blending, foot planting and timing. We share what we learned from the sessions and how it shapes the way our own animators work each day.</p>
      <a class="read-more" href="#">READ MORE</a>
    </article>
    <article class="post-card">
      <p class="post-date">06.05.2014</p>
      <h2 class="post-title">Vivamus quis mattis quam, id congue tortu</h2>
      <p class="post-excerpt">A short look at how we plan each week, review our builds and keep quality high. Small habits add up, and we think they are worth sharing with anyone who cares about the craft.</p>
      <a class="read-more" href="#">READ MORE</a>
    </article>
    <article class="post-card">
      <p class="post-date">29.04.2014</p>
      <h2 class="post-title">Nam accumsan eget orci sed tincidunt ultricies</h2>
      <p class="post-excerpt">We are growing the team and looking for people who love precise, careful work. Read about the roles we have open and what a normal day in our small studio looks like right now.</p>
      <a class="read-more" href="#">READ MORE</a>
    </article>
    <article class="post-card">
      <p class="post-date">22.04.2014</p>
      <h2 class="post-title">Pellentesque vel gravida neque</h2>
      <p class="post-excerpt">Notes on lighting a quiet scene so that it reads like film. We compare early tests with our current look and explain the trade-offs we made to keep every frame clear and calm.</p>
      <a class="read-more" href="#">READ MORE</a>
    </article>
  </div>
  <div class="earth-bottom" role="img" aria-label="Rough earth-toned texture band"></div>
</section>
<p class="caption caption--all">View all post (Blog section are expanded)</p>

</body>
</html>
```